Exploding Software Company Needs a New Age Business Card Designed

We are in need of new business cards for our software company, Northgate Digital Works LLC, that specializes in web-based construction software. We have a software as a subscription called "Quarrymint" that is growing fast and we want business cards to be cutting edge like our software. We need to use our current logo and would like a QR code to scan. The tricky part to me is that we preach paperless with our software and electronic document management but still need business cards in today's market at times.
Updates

Need to have the QR code on the design. 

Add yellow or orange color to enhance the look.

Quarrymint is the key name but need to have the name of the company "Northgate Digital Works LLC" on the card too.

Target Market(s)

Our target market is the construction market that can range from people that are 20 to 65 years old. Most are men but more and more women are coming on.

Industry/Entity Type

Business

Requirements
Must have
• Must incorporate the logo for the software "Quarrymint". The logo is just the symbol. Change the Quarrymint word so it is easily legible.
Nice to have
• A "QR" code that can be scanned for the basic contact information such as company name, website, contact name, email and phone.

```html
<!DOCTYPE html>
<html lang="en">
<head>
<meta charset="utf-8">
<title>Quarrymint Business Card</title>
<link rel="stylesheet" href="https://fonts.googleapis.com/css2?family=Alegreya:wght@400;700&family=Alegreya+Sans:wght@700&display=swap">
<style>
  :root {
    --backdrop: #6e6e6c;
    --card-white: #ffffff;
    --card-light: #e7e7e7;
    --band-grey: #9a9a9a;
    --ink: #5a5a5a;
    --ink-soft: #6a6a6a;
    --mark-blue: #9aa6b6;
    --accent: #f39a1e;
    --qr-dark: #4a4a4a;
  }
  * { margin: 0; padding: 0; box-sizing: border-box; }
  html, body { width: 1200px; height: 848px; overflow: hidden; }
  body {
    background: var(--backdrop);
    font-family: "Alegreya", Georgia, serif;
    color: var(--ink);
    position: relative;
  }
  .card {
    position: absolute;
    width: 380px;
    height: 234px;
    overflow: hidden;
    box-shadow: 0 6px 18px rgba(0,0,0,0.25);
  }
  .card-back { left: 160px; top: 330px; background: var(--band-grey); }
  .card-front { left: 557px; top: 378px; background: var(--card-white); }
  .card svg.shape { position: absolute; inset: 0; }

  .back-mark {
    position: absolute;
    left: 0; right: 0; top: 92px;
    display: flex; align-items: center; justify-content: center; gap: 10px;
  }
  .back-mark .dot {
    width: 22px; height: 22px; border-radius: 50%;
    background: var(--mark-blue);
  }
  .back-mark .name {
    font-family: "Alegreya Sans", Arial, sans-serif;
    font-weight: 700; font-size: 38px; color: var(--mark-blue);
  }

  .brand-title {
    position: absolute; left: 9px; top: 2px;
    font-weight: 700; font-size: 24px; letter-spacing: 1px;
    font-variant: small-caps; color: var(--ink);
  }
  .brand-rule {
    position: absolute; left: 10px; top: 34px;
    width: 130px; height: 3px; background: var(--accent);
  }
  .front-mark {
    position: absolute; left: 10px; top: 96px;
    display: flex; align-items: center; gap: 7px;
  }
  .front-mark .dot {
    width: 16px; height: 16px; border-radius: 50%; background: var(--mark-blue);
  }
  .front-mark .name {
    font-family: "Alegreya Sans", Arial, sans-serif;
    font-weight: 700; font-size: 20px; color: var(--mark-blue);
  }
  .person {
    position: absolute; left: 163px; top: 40px;
    font-weight: 700; font-size: 15px; color: var(--ink);
    white-space: nowrap;
  }
  .person .role { font-size: 11px; }
  .contact {
    position: absolute; left: 188px; top: 74px;
    font-weight: 700; font-size: 11.5px; line-height: 15px; color: var(--ink-soft);
  }
  .offices-title {
    margin-top: 10px; display: inline-block;
    border-bottom: 1px solid var(--accent); padding-right: 28px;
  }
  .offices { list-style: none; }
  .offices li::before { content: "\2022"; }
  .qr-code {
    position: absolute; right: 12px; top: 104px;
    width: 50px; height: 50px;
    background: var(--qr-dark);
    border: 4px solid var(--card-white);
    outline: 1px solid var(--card-light);
  }
  .website {
    position: absolute; left: 8px; top: 196px;
    font-weight: 700; font-size: 13px; color: var(--card-white);
  }
  .company {
    position: absolute; right: 10px; top: 214px;
    font-weight: 700; font-size: 10px; color: var(--card-white);
  }
</style>
</head>
<body>
  <section class="card card-back">
    <svg class="shape" width="380" height="234" viewBox="0 0 380 234">
      <path d="M50 234 C72 126 162 28 300 0 L362 0 C318 54 300 153 308 234 Z" fill="var(--card-light)"/>
    </svg>
    <div class="back-mark">
      <span class="dot"></span>
      <span class="name">Quarrymint</span>
    </div>
  </section>

  <section class="card card-front">
    <svg class="shape" width="380" height="234" viewBox="0 0 380 234">
      <path d="M0 172 C120 160 260 168 380 212 L380 234 L0 234 Z" fill="var(--band-grey)"/>
      <path d="M0 172 C120 160 260 168 380 212" fill="none" stroke="var(--accent)" stroke-width="3"/>
    </svg>
    <h1 class="brand-title">Quarrymint</h1>
    <div class="brand-rule"></div>
    <div class="front-mark">
      <span class="dot"></span>
      <span class="name">Quarrymint</span>
    </div>
    <p class="person">Dana Whitlock <span class="role">, P.E. - President</span></p>
    <div class="contact">
      <p>888-555-0147, ext. 103</p>
      <p>dana@quarrymint.com</p>
      <p class="offices-title">Office Locations :</p>
      <ul class="offices">
        <li>Lakeview, WI</li>
        <li>Redstone, AZ</li>
      </ul>
    </div>
    <div class="qr-code" role="img" aria-label="QR code with contact details"></div>
    <p class="website">www.quarrymint.com</p>
    <p class="company">Northgate Digital Works LLC</p>
  </section>
</body>
</html>
```